A Label for an ECO Friendly Spirit Company

Design a label which can be used for vodka and gin (London Dry Gin). It should be Square type Like the Shape File you see in the uploads. VORK means Local Eco friendly Authentic and Fair. We want a cool and slim label that calls for eco-friendly. We want to use it for our premium
Vodka and our London Dry Gin. Please use the logo and design it in Square Type.

40%vol, 700ml

Target Market(s)

spirits and events

Industry/Entity Type

SPIRITS

Colors
00AB8E
00BBA5
67D7C9
C6EFE9
E9F9F6
59FF00
82FF00
B8FF75
E3FFCB
F4FFEA

Requirements
Must have
• Logo from VORK, Squaee Shape

```html
<!DOCTYPE html>
<html lang="en">
<head>
<meta charset="utf-8">
<title>VORK Vodka and Gin Label</title>
<link rel="stylesheet" href="https://fonts.googleapis.com/css2?family=Nunito:wght@800;900&family=Roboto+Slab:wght@400;700&family=Noto+Serif:wght@400&display=swap">
<style>
  :root {
    --backdrop: #a4a4a4;
    --label-green: #8cc63f;
    --label-teal: #00ab8e;
    --ink-white: #ffffff;
    --band-text: #7cbf2e;
  }
  html, body {
    margin: 0;
    padding: 0;
    width: 1200px;
    height: 2452px;
    overflow: hidden;
    background: var(--backdrop);
  }
  .canvas {
    position: relative;
    width: 1200px;
    height: 2452px;
  }
  .label-shape {
    position: absolute;
    left: 120px;
    top: 746px;
    width: 960px;
    height: 960px;
  }
  .label-content {
    position: absolute;
    left: 120px;
    top: 746px;
    width: 960px;
    height: 960px;
    color: var(--ink-white);
    text-align: center;
  }
  .brand {
    position: absolute;
    left: 0;
    right: 0;
    top: 220px;
    display: flex;
    justify-content: center;
    align-items: center;
    gap: 18px;
  }
  .brand-dot {
    width: 52px;
    height: 52px;
    border-radius: 50%;
    background: var(--ink-white);
  }
  .brand-name {
    font-family: "Nunito", sans-serif;
    font-weight: 900;
    font-size: 76px;
    letter-spacing: 2px;
    line-height: 1;
    color: var(--ink-white);
  }
  .product-title {
    position: absolute;
    left: 0;
    right: 0;
    top: 390px;
    margin: 0;
    font-family: "Nunito", sans-serif;
    font-weight: 900;
    font-size: 84px;
    line-height: 1;
    color: var(--ink-white);
  }
  .product-title .joiner {
    color: var(--label-teal);
  }
  .spec-band {
    position: absolute;
    left: 220px;
    width: 520px;
    top: 510px;
    height: 44px;
    background: var(--ink-white);
    font-family: "Roboto Slab", serif;
    font-weight: 700;
    font-size: 28px;
    line-height: 44px;
    color: var(--band-text);
  }
  .variety {
    position: absolute;
    left: 0;
    right: 0;
    top: 585px;
    font-family: "Roboto Slab", serif;
    font-weight: 400;
    font-size: 20px;
    letter-spacing: 3px;
    color: var(--ink-white);
  }
  .description {
    position: absolute;
    left: 310px;
    width: 340px;
    top: 640px;
    margin: 0;
    font-family: "Noto Serif", serif;
    font-size: 23px;
    line-height: 1.3;
    color: var(--ink-white);
  }
</style>
</head>
<body>
<div class="canvas">
  <svg class="label-shape" viewBox="0 0 960 960" aria-hidden="true">
    <polygon points="480,0 960,480 480,960 0,480" fill="var(--label-green)"/>
    <polygon points="480,30 930,480 480,930 30,480" fill="none" stroke="var(--ink-white)" stroke-width="3" stroke-dasharray="12 9"/>
  </svg>
  <div class="label-content">
    <div class="brand">
      <span class="brand-dot"></span>
      <span class="brand-name">VORK</span>
    </div>
    <h1 class="product-title">Vodka <span class="joiner">and</span> Gin</h1>
    <div class="spec-band">40%vol, 700ml SPIRITS</div>
    <div class="variety">LONDON DRY GIN</div>
    <p class="description">Lorem Ipsum is simply dummy text of the printing and typesetting industry. Loremspecimen book.</p>
  </div>
</div>
</body>
</html>
```